Creative packaging for Scandinavian Coffee brand

Vårk is a new-to-the-world Scandinavian coffee brand, offering a top-quality instant coffee product laden with health benefits. The ‘coffee moment’ is a sacred part of life in Scandinavia: it represents a pause from the day – a peaceful, quiet break in which you detach, sit back and just focus on being present for a while. The success of Vårk will be built on two critical drivers: 1) a delicious product, and 2) a modern “love brand”, which young consumers will identify with and be proud to display on their shelves.
We want Vårk packaging design and branding to be a visually stunning representation of our brand values of savour, sustainability and authenticity – and convey a strong link back to our Scandinavian heritage.
The packaging we are looking for should be:
Product: 500ml container of instant coffee
Packaging design (3D): we welcome unusual shapes/materials to help us stand out at shelf and convey a premium/modern look & feel. However, the pack should still be a) practical for shipping (i.e. not too fragile or complicated to pack in large quantities) and b) sustainable.
Artwork (2D): should look modern/sophisticated/minimalist (think: Scandinavian design) – but ideally with a unique twist that helps it stand out at shelf. Preferred dominant colours are whites or blacks. Artwork must include the logo (attached, can be either black on white or white on black).
Optional: we will also be selling single-serve packets to go with the 500ml packet, which could be sold either in sachets, capsules or other interesting packaging, with a consistent look & feel as the main packet.
We hope to stand out in a crowded category – so please feel free to stretch your imagination beyond what is currently available on shelf! (we've attached an example of a typical instant coffee shelf for perspective)
Target Market(s)
Millennial / young consumers, who are willing to spend a little extra for an appealing design

```html
<!DOCTYPE html>
<html lang="en">
<head>
<meta charset="utf-8">
<title>Vårk Black Coffee – Box Dieline</title>
<link rel="stylesheet" href="https://fonts.googleapis.com/css2?family=Libre+Baskerville:wght@700&family=Oswald:wght@300;400&family=Lato:wght@300&display=swap">
<style>
  :root{
    --canvas:#ffffff;
    --paper:#ffffff;
    --ink:#000000;
    --white:#ffffff;
    --copper:#b0592c;
    --leaf:#5f7f52;
    --berry:#b8423c;
    --crema:#c98a4b;
    --bean:#7a4a2a;
    --line:#6e6e6e;
  }
  *{box-sizing:border-box;margin:0;padding:0}
  html,body{width:1200px;height:1200px;overflow:hidden}
  body{background:var(--canvas);position:relative;font-family:"Lato",sans-serif}

  .dieline{position:absolute;left:50px;top:297px;width:1100px;height:606px;display:flex;border:1px solid var(--line)}

  .front-panel{position:relative;width:380px;height:100%;background:var(--paper);overflow:hidden}
  .spine-panel{position:relative;width:170px;height:100%;background:var(--ink);color:var(--white);text-align:center}

  .art{position:absolute}
  .art-leaves-left{left:0;top:55px;width:42px;height:290px;
    background:linear-gradient(180deg,rgba(255,255,255,0) 0%,var(--leaf) 18%,#f1f1e8 42%,var(--leaf) 58%,var(--berry) 74%,rgba(255,255,255,0) 100%);opacity:.7}
  .art-leaves-right{left:335px;top:80px;width:45px;height:235px;
    background:linear-gradient(180deg,var(--leaf) 0%,#f4f4ee 40%,var(--leaf) 70%,rgba(255,255,255,0) 100%);opacity:.7}
  .art-cup{left:0;top:455px;width:138px;height:138px;border-radius:50%;
    background:radial-gradient(circle at 50% 50%,#f2dcc0 0%,var(--crema) 40%,#a86a34 62%,#f5ece2 76%,rgba(255,255,255,0) 100%)}
  .art-beans{left:145px;top:410px;width:235px;height:196px;
    background:radial-gradient(ellipse at 72% 62%,var(--bean) 0%,#9a6438 38%,rgba(190,140,100,.35) 62%,rgba(255,255,255,0) 80%)}

  .front-label{position:absolute;left:42px;top:36px;width:294px;height:419px;background:var(--ink);color:var(--white);text-align:center;z-index:2}
  .front-label > *{position:absolute;left:0;right:0}

  .brand-name{font-family:"Lato",sans-serif;font-weight:300;letter-spacing:.12em;line-height:1;color:var(--white)}
  .product-title{font-family:"Libre Baskerville",serif;font-weight:700;color:var(--copper)}
  .claim{font-family:"Oswald",sans-serif;font-weight:400;line-height:1}
  .origin{font-family:"Lato",sans-serif;font-weight:300;line-height:1}
  .format{font-family:"Oswald",sans-serif;font-weight:300;font-size:12px;line-height:18px}
  .weight{font-family:"Oswald",sans-serif;font-weight:300;font-size:10px;line-height:1}

  .front-label .brand-name{top:30px;font-size:44px}
  .front-label .product-title{top:110px;font-size:36px;line-height:40px}
  .divider{top:204px;display:flex;align-items:center;justify-content:center;gap:12px}
  .divider-rule{width:52px;height:1.5px;background:var(--white)}
  .front-label .claim{top:266px;font-size:21px}
  .front-label .origin{top:293px;font-size:15px}
  .front-label .format{top:342px}
  .front-label .weight{top:402px}

  .spine-panel > *{position:absolute;left:0;right:0}
  .spine-panel .brand-name{top:36px;font-size:44px}
  .spine-title{left:50%!important;right:auto!important;top:342px;font-size:33px;line-height:1;white-space:nowrap;
    transform:translate(-50%,-50%) rotate(-90deg)}
  .spine-panel .claim{top:507px;font-size:21px}
  .spine-panel .origin{top:540px;font-size:15px}
  .spine-panel .weight{top:579px}
</style>
</head>
<body>
  <main class="dieline">
    <section class="front-panel">
      <div class="art art-leaves-left" role="img" aria-label="Watercolour coffee branch with leaves, white blossoms and red cherries"></div>
      <div class="art art-leaves-right" role="img" aria-label="Watercolour coffee leaves and white blossoms"></div>
      <div class="art art-cup" role="img" aria-label="Watercolour cup of latte with leaf latte art, seen from above"></div>
      <div class="art art-beans" role="img" aria-label="Watercolour roasted coffee beans spilling from a wooden scoop"></div>
      <div class="front-label">
        <p class="brand-name">Vårk</p>
        <h1 class="product-title">BLACK<br>COFFEE</h1>
        <div class="divider">
          <span class="divider-rule"></span>
          <svg width="20" height="22" viewBox="0 0 34 34" aria-hidden="true">
            <ellipse cx="17" cy="17" rx="12" ry="15" fill="#fff"/>
            <path d="M17 3 C10 11 24 22 17 31" stroke="#000" stroke-width="2.6" fill="none"/>
          </svg>
          <span class="divider-rule"></span>
        </div>
        <p class="claim">Premium Coffe</p>
        <p class="origin">100% Scandinavian</p>
        <p class="format">INSTANT AND<br>MICROGROUND COFFE</p>
        <p class="weight">500 gms</p>
      </div>
    </section>

    <section class="spine-panel">
      <p class="brand-name">Vårk</p>
      <p class="product-title spine-title">BLACK COFFEE</p>
      <p class="claim">Premium Coffe</p>
      <p class="origin">100% Scandinavian</p>
      <p class="weight">500 gms</p>
    </section>

    <section class="front-panel">
      <div class="art art-leaves-left" role="img" aria-label="Watercolour coffee branch with leaves, white blossoms and red cherries"></div>
      <div class="art art-leaves-right" role="img" aria-label="Watercolour coffee leaves and white blossoms"></div>
      <div class="art art-cup" role="img" aria-label="Watercolour cup of latte with leaf latte art, seen from above"></div>
      <div class="art art-beans" role="img" aria-label="Watercolour roasted coffee beans spilling from a wooden scoop"></div>
      <div class="front-label">
        <p class="brand-name">Vårk</p>
        <p class="product-title">BLACK<br>COFFEE</p>
        <div class="divider">
          <span class="divider-rule"></span>
          <svg width="20" height="22" viewBox="0 0 34 34" aria-hidden="true">
            <ellipse cx="17" cy="17" rx="12" ry="15" fill="#fff"/>
            <path d="M17 3 C10 11 24 22 17 31" stroke="#000" stroke-width="2.6" fill="none"/>
          </svg>
          <span class="divider-rule"></span>
        </div>
        <p class="claim">Premium Coffe</p>
        <p class="origin">100% Scandinavian</p>
        <p class="format">INSTANT AND<br>MICROGROUND COFFE</p>
        <p class="weight">500 gms</p>
      </div>
    </section>

    <section class="spine-panel">
      <p class="brand-name">Vårk</p>
      <p class="product-title spine-title">BLACK COFFEE</p>
      <p class="claim">Premium Coffe</p>
      <p class="origin">100% Scandinavian</p>
      <p class="weight">500 gms</p>
    </section>
  </main>
</body>
</html>
```